Quillby Systems Business Card

Create an appealing and elegant Business card for quillby systems. Include logo and use related colors from website, be creative. Include Business name, my name, tile, address, contacts, address, and social media contacts if possible. Logo PSD file is attached.

Bleed Area: 3.46" x 2.32"
Trim: 3.3" x 2.16"
Safe Area: 3.14" x 2.02"

Save files as vector-based PDF with outlined text and PNG.
No crop marks
CMYK color setting

Business Card Info:

Quillby Systems

Dorian Vellacott
Owner

418 Bramlow Rd Unit C
Harlow Falls, VT 02771
t. 1.888.562.3907
e. dorian.v@quillbysys.example
w. www.quillbysys.example

facebook. www.facebook.com/QuillbySys
twitter. twitter.com/quillbysys
pinterest. www.pinterest.com/quillbysys/

Target Market(s)

Business Owners and Partners

Industry/Entity Type

Business

Requirements
Must have
• Logo and related colors from website

```html
<!DOCTYPE html>
<html lang="en">
<head>
<meta charset="utf-8">
<title>Quillby Systems Business Card</title>
<link rel="stylesheet" href="https://fonts.googleapis.com/css2?family=Open+Sans:wght@400;600&display=swap">
<style>
  :root {
    --page: #e6e8eb;
    --paper: #ffffff;
    --brand-blue: #4b76a9;
    --ink: #141414;
    --on-blue: #ffffff;
  }
  * { margin: 0; padding: 0; box-sizing: border-box; }
  html, body { width: 1200px; height: 780px; overflow: hidden; }
  body {
    background: var(--page);
    font-family: "Open Sans", Arial, sans-serif;
    position: relative;
  }
  .card {
    position: absolute;
    top: 213px;
    width: 540px;
    height: 353px;
    background: var(--paper);
    overflow: hidden;
    box-shadow: 0 6px 18px rgba(0,0,0,.18);
  }
  .card--front { left: 40px; }
  .card--back { left: 620px; }
  .card__art { position: absolute; inset: 0; width: 100%; height: 100%; }

  .brand-name {
    position: absolute;
    color: var(--ink);
    font-weight: 600;
    line-height: 1.02;
    display: flex;
    align-items: center;
    gap: 10px;
  }
  .brand-name__dot {
    width: 14px; height: 14px; border-radius: 50%;
    background: var(--brand-blue);
    flex: none;
  }
  .card--front .brand-name { left: 44px; top: 118px; font-size: 44px; }
  .card--back .brand-name { left: 26px; top: 26px; font-size: 25px; }

  .social-list {
    position: absolute; left: 26px; bottom: 24px;
    list-style: none; font-size: 10.5px; color: var(--ink);
  }
  .social-list li { display: flex; align-items: center; gap: 6px; margin-top: 3px; }
  .social-list__mark { width: 9px; height: 9px; border-radius: 50%; background: var(--brand-blue); }

  .holder {
    position: absolute; right: 28px; top: 26px; width: 230px;
    color: var(--on-blue); text-align: left;
  }
  .holder__name { font-size: 22px; font-weight: 400; letter-spacing: .3px; }
  .holder__title { font-size: 11px; margin-top: 1px; }
  .holder__rule { height: 1.5px; background: var(--on-blue); margin-top: 4px; }

  .contact-list {
    position: absolute; right: 28px; top: 130px; width: 230px;
    list-style: none; color: var(--on-blue); font-size: 12.5px; line-height: 1.3;
  }
  .contact-list li { display: flex; align-items: flex-start; gap: 9px; margin-bottom: 6px; }
  .contact-list svg { width: 14px; height: 14px; flex: none; margin-top: 2px; }
</style>
</head>
<body>

<section class="card card--front" aria-label="Card front">
  <svg class="card__art" viewBox="0 0 540 353" aria-hidden="true">
    <path d="M345 0 C 430 70, 400 250, 270 353 L540 353 L540 0 Z" fill="var(--brand-blue)"/>
    <path d="M262 353 C 390 260, 420 140, 372 30 C 392 150, 360 270, 292 353 Z" fill="var(--ink)"/>
  </svg>
  <div class="brand-name"><span class="brand-name__dot"></span><span>Quillby<br>Systems</span></div>
</section>

<section class="card card--back" aria-label="Card back">
  <svg class="card__art" viewBox="0 0 540 353" aria-hidden="true">
    <path d="M180 0 L540 0 L540 353 L285 353 C 245 250, 255 150, 180 0 Z" fill="var(--brand-blue)"/>
    <path d="M160 0 C 238 140, 222 250, 262 353 L285 353 C 240 250, 250 140, 180 0 Z" fill="var(--ink)"/>
  </svg>

  <div class="brand-name"><span class="brand-name__dot"></span><span>Quillby<br>Systems</span></div>

  <ul class="social-list">
    <li><span class="social-list__mark"></span>/QuillbySys</li>
    <li><span class="social-list__mark"></span>/quillbysys</li>
    <li><span class="social-list__mark"></span>/quillbysys</li>
  </ul>

  <div class="holder">
    <p class="holder__name">Dorian Vellacott</p>
    <p class="holder__title">Owner</p>
    <div class="holder__rule"></div>
  </div>

  <ul class="contact-list">
    <li>
      <svg viewBox="0 0 14 14"><path d="M3 1.5 L5.5 1.5 L6.5 4.5 L5 5.8 C5.8 7.5 6.6 8.3 8.2 9 L9.5 7.5 L12.5 8.5 L12.5 11 C12.5 12 11.5 12.5 10.5 12.5 C5.5 12 2 8.5 1.5 3.5 C1.5 2.5 2 1.5 3 1.5 Z" fill="var(--on-blue)"/></svg>
      <span>1.888.562.3907</span>
    </li>
    <li>
      <svg viewBox="0 0 14 14"><circle cx="7" cy="7" r="5.5" fill="none" stroke="var(--on-blue)" stroke-width="1.4"/><circle cx="7" cy="7" r="2.2" fill="none" stroke="var(--on-blue)" stroke-width="1.4"/></svg>
      <span>dorian.v@quillbysys.example</span>
    </li>
    <li>
      <svg viewBox="0 0 14 14"><circle cx="7" cy="7" r="5.5" fill="none" stroke="var(--on-blue)" stroke-width="1.2"/><ellipse cx="7" cy="7" rx="2.4" ry="5.5" fill="none" stroke="var(--on-blue)" stroke-width="1"/><line x1="1.5" y1="7" x2="12.5" y2="7" stroke="var(--on-blue)" stroke-width="1"/></svg>
      <span>www.quillbysys.example</span>
    </li>
    <li>
      <svg viewBox="0 0 14 14"><path d="M7 13 C4 9 2.5 7 2.5 5 A4.5 4.5 0 0 1 11.5 5 C11.5 7 10 9 7 13 Z" fill="var(--on-blue)"/><circle cx="7" cy="5" r="1.6" fill="var(--brand-blue)"/></svg>
      <span>418 Bramlow Rd Unit C<br>Harlow Falls, VT 02771</span>
    </li>
  </ul>
</section>

</body>
</html>
```